Beer Can Label design - HAZY NEIPA

Hazy NEIPA. (Acronym for New England India Pale Ale)
Full sleeve (473ml)
5.00" x 8.125" Inches
Write up on can reverse.
Opaque haze in appearance derived from specific oats, wheat, and water chemistry. This brew bolsters a dense and creamy head, leaving behind a soft and silky mouth-feel. Expect an intense tropical fruit centric aroma and flavour. Our timely hop additions contributes to less bitterness than typical IPA’s.
Logo is to be on front, towards bottom. Title near top.
Looking for something that stands out. Bold.
Target Market(s)
Craft beer enthusiasts
Industry/Entity Type
Beer & Brewing
Requirements
Must have
- Eye catching.

```html
<!DOCTYPE html>
<html lang="en">
<head>
<meta charset="utf-8">
<title>Ironvale Brew House – Hazy NEIPA label</title>
<link href="https://fonts.googleapis.com/css2?family=Oswald:wght@300;400;500;700&display=swap" rel="stylesheet">
<style>
  :root {
    --lime: #a3c614;
    --lime-panel: #9cc012;
    --lime-dark: #74a80a;
    --white: #ffffff;
    --paper: #ffffff;
  }
  * { margin: 0; padding: 0; box-sizing: border-box; }
  html, body { width: 1200px; height: 1200px; overflow: hidden; background: var(--paper); }
  body { position: relative; font-family: "Oswald", sans-serif; color: var(--white); }

  .label {
    position: absolute; left: 95px; top: 294px; width: 1012px; height: 618px;
    background: var(--lime); overflow: hidden;
  }
  .skyline {
    position: absolute; left: 0; right: 0; bottom: 0; height: 100px;
    background: linear-gradient(to bottom, #86b20f, var(--lime-dark) 35%);
  }

  .side-title {
    position: absolute; left: 78px; top: 580px; width: 520px;
    transform: rotate(-90deg); transform-origin: left top;
    font-weight: 700; font-size: 100px; line-height: 0.98; text-transform: uppercase;
    letter-spacing: 1px;
  }

  .front {
    position: absolute; left: 390px; top: 0; width: 238px; height: 100%;
    background: var(--lime-panel); overflow: hidden;
    box-shadow: -14px 0 24px rgba(0,0,0,0.08), 14px 0 24px rgba(0,0,0,0.08);
  }

  .title-group {
    position: absolute; left: -30px; top: 100px; width: 298px;
    transform: rotate(-14deg); transform-origin: center center;
  }
  .title-band {
    height: 82px; background: var(--white); color: var(--lime-panel);
    display: flex; align-items: center; justify-content: center; gap: 8px;
    padding-top: 2px;
  }
  .title-band .small { font-weight: 700; font-size: 24px; line-height: 1; letter-spacing: 7px; }
  .title-band .big { font-weight: 700; font-size: 70px; line-height: 1; }
  .title-heads {
    text-align: center; font-weight: 700; font-size: 72px; line-height: 1.1;
  }

  .brand {
    position: absolute; left: 0; top: 360px; width: 238px;
    display: flex; align-items: center; justify-content: center; gap: 10px;
  }
  .brand-dot { width: 18px; height: 18px; border-radius: 50%; background: var(--white); }
  .brand-name { font-weight: 500; font-size: 30px; line-height: 1.05; text-transform: uppercase; text-align: left; }
  .style-name {
    position: absolute; left: 0; top: 518px; width: 238px; text-align: center;
    font-weight: 700; font-size: 24px;
  }
  .style-rule { position: absolute; left: 22px; top: 553px; width: 194px; height: 1px; background: var(--white); }
  .strength {
    position: absolute; left: 0; top: 558px; width: 238px; text-align: center;
    font-weight: 400; font-size: 19px;
  }

  .write-up {
    position: absolute; left: 724px; top: 64px; width: 240px;
    font-weight: 300; font-size: 24px; line-height: 33px;
  }
  .write-up p + p { margin-top: 33px; }
  .write-up strong { font-weight: 700; }
</style>
</head>
<body>
  <section class="label">
    <div class="skyline" role="img" aria-label="Industrial city skyline silhouette in dark green"></div>

    <h2 class="side-title">For the<br>Hop Heads!</h2>

    <div class="front">
      <div class="skyline" role="img" aria-label="Industrial city skyline silhouette in dark green"></div>
      <div class="title-group">
        <div class="title-band"><span class="small">FOR<br>THE</span><span class="big">HOP</span></div>
        <div class="title-heads">HEADS!</div>
      </div>
      <div class="brand">
        <span class="brand-dot"></span>
        <span class="brand-name">Ironvale<br>Brew House</span>
      </div>
      <div class="style-name">Hazy NEIPA</div>
      <div class="style-rule"></div>
      <div class="strength">Stong Beer/Bière forte</div>
    </div>

    <div class="write-up">
      <p><strong>Opaque haze</strong> in appearance derived from specific oats, wheat, and water chemistry. This brew bolsters a dense and creamy head, leaving behind a soft and silky mouth-feel.</p>
      <p>Expect an intense tropi-cal fruit centric aroma and flavour. Our timely hop additions contrib-utes to less bitterness than typical IPA’s.</p>
    </div>
  </section>
</body>
</html>
```